Velmora Partners - website for real estate investment company

Create a bold, modern website that reflects Velmora’s success, professionalism, and credibility.
The design must stand out while maintaining a polished, corporate tone. (bold, but understated)
The client just created a new logo, and the website design must be in sync with the logo design. Information about the logo colors, fonts, and message are in the attached design brief.
Updates

Target Market(s)

b2b: banks, brokers, institutional partners, vendors, and property sellers.

Industry/Entity Type

real estate investment company

Number of Pages Required

1 page

Font styles to use
Sans Serif

Colors

Designer to choose colors to be used in the design.

Requirements
Must have
• 1. homepage design (psd) 2. a top banner image (psd) for a default inner page
Nice to have
• please see attached design brief
Should not have

```html
<!DOCTYPE html>
<html lang="en">
<head>
<meta charset="utf-8">
<title>Velmora Partners</title>
<link href="https://fonts.googleapis.com/css2?family=Barlow+Semi+Condensed:wght@700;800&family=Poppins:wght@400;500;600&display=swap" rel="stylesheet">
<style>
:root{
  --red:#dc1e28;
  --ink:#1d1d1f;
  --slate:#4a4a4c;
  --mist:#f4f4f4;
  --white:#ffffff;
  --display:"Barlow Semi Condensed",sans-serif;
  --body:"Poppins",sans-serif;
}
*{margin:0;padding:0;box-sizing:border-box}
html,body{width:1200px;height:3005px;overflow:hidden;background:var(--white);font-family:var(--body);color:var(--ink)}
.page{position:relative;width:1200px;height:3005px;overflow:hidden}
.abs{position:absolute}

/* header */
.brand{left:68px;top:28px;font-family:var(--display);font-weight:800;font-size:78px;line-height:1;color:var(--slate);letter-spacing:1px}
.mail-chip{left:824px;top:25px;display:flex;align-items:center;gap:9px;white-space:nowrap}
.mail-chip .ico{width:28px;height:28px;background:var(--slate);border-radius:3px;display:flex;align-items:center;justify-content:center}
.mail-chip small{display:block;color:var(--red);font-size:14px;line-height:16px}
.mail-chip span{font-size:14px;line-height:16px;color:var(--ink)}
.btn-contact{left:998px;top:21px;width:135px;height:37px;border-radius:19px;background:var(--red);color:var(--white);font-weight:600;font-size:14px;display:flex;align-items:center;justify-content:center;letter-spacing:.5px}
.main-nav{left:455px;top:79px;display:flex;gap:38px;font-size:13.5px;text-transform:uppercase;white-space:nowrap}
.main-nav a{color:var(--ink);text-decoration:none;padding:0 0 10px}
.main-nav a.current{color:var(--red);border-bottom:2px solid var(--red);padding:0 9px 10px}

/* hero */
.hero{left:0;top:127px;width:1200px;height:794px;background:linear-gradient(180deg,#c89a5e 0%,#8d7462 25%,#4a4646 50%,#2c2c2e 75%,#232325 100%)}
.hero h1{position:absolute;left:0;top:491px;width:1200px;text-align:center;font-family:var(--display);font-weight:800;font-size:70px;line-height:1;color:var(--white);letter-spacing:1px;white-space:nowrap}
.hero h1 em{font-style:normal;color:var(--red)}
.hero p{position:absolute;left:95px;top:579px;width:1010px;text-align:center;font-size:22.5px;line-height:36px;color:var(--white)}

/* stats */
.stat{width:260px;text-align:center}
.stat .num{font-weight:600;font-size:42px;line-height:1;color:var(--ink)}
.stat .bar{width:78px;height:3px;background:var(--red);margin:17px auto 0}
.stat .lbl{margin-top:26px;font-size:14.5px;line-height:21px;text-transform:uppercase}

/* sectors */
.sector{top:1366px;height:400px;overflow:hidden}
.sector .band{position:absolute;left:0;top:159px;width:100%;height:78px;background:rgba(40,40,42,.75);display:flex;align-items:center;justify-content:center;font-family:var(--display);font-weight:800;font-size:27px;color:var(--white);letter-spacing:1px}

/* contact */
.contact{left:0;top:1894px;width:1200px;height:639px;background:linear-gradient(160deg,#3a3b3d 0%,#2a2b2d 50%,#1f2022 100%)}
.contact h2{position:absolute;left:239px;top:180px;font-family:var(--display);font-weight:800;font-size:60px;line-height:1;color:var(--white);letter-spacing:1px}
.contact h2 em{font-style:normal;color:var(--red)}
.field{position:absolute;background:var(--white);border:1px solid #d8d8d8;font-size:11.5px;color:#666;padding:13px 18px}
.submit{position:absolute;left:303px;top:485px;width:165px;height:47px;border-radius:24px;background:var(--red);color:var(--white);font-weight:600;font-size:16px;display:flex;align-items:center;padding-left:31px}
.submit .ring{position:absolute;right:4px;top:3px;width:41px;height:41px;border:2px solid var(--white);border-radius:50%;display:flex;align-items:center;justify-content:center}

/* footer */
.footer{left:0;top:2533px;width:1200px;height:472px;background:var(--mist)}
.foot-brand{position:absolute;left:0;top:96px;width:1200px;text-align:center;font-family:var(--display);font-weight:800;font-size:112px;line-height:1;color:var(--slate);letter-spacing:2px}
.info{position:absolute;top:252px;display:flex;gap:12px;align-items:center;font-size:14.5px;line-height:21px;white-space:nowrap}
.info .pin{width:34px;height:34px;background:var(--red);border-radius:4px;display:flex;align-items:center;justify-content:center}
.rule{position:absolute;left:74px;width:1063px;height:1px;background:var(--red)}
.foot-nav{position:absolute;left:0;top:362px;width:1200px;display:flex;justify-content:center;gap:38px;font-size:14px;font-weight:500;text-transform:uppercase}
.foot-nav i{font-style:normal}
.copy{position:absolute;left:67px;top:436px;font-size:12.5px}
.socials{position:absolute;left:1017px;top:430px;display:flex;gap:6px}
.socials span{width:26px;height:26px;background:var(--red);border-radius:3px}
</style>
</head>
<body>
<div class="page">

  <!-- header -->
  <div class="abs brand">VELMORA</div>
  <div class="abs mail-chip">
    <div class="ico"><svg width="16" height="12" viewBox="0 0 16 12"><rect x=".5" y=".5" width="15" height="11" fill="#fff"/><path d="M1 1l7 6 7-6" fill="none" stroke="#4a4a4c" stroke-width="1.4"/></svg></div>
    <div><small>Email Us</small><span>info@velmora.com</span></div>
  </div>
  <div class="abs btn-contact">CONTACT</div>
  <nav class="abs main-nav">
    <a class="current">Home</a><a>Our Story</a><a>Investment Strategy</a><a>What Sets Us Apart</a><a>Our Portfolio</a>
  </nav>

  <!-- hero -->
  <section class="abs hero" role="img" aria-label="City skyline at sunset with a tall spire tower">
    <svg class="abs" style="left:0;top:0" width="260" height="262"><polygon points="0,0 260,0 0,262" fill="#dc1e28"/></svg>
    <svg class="abs" style="left:543px;top:347px" width="114" height="114" viewBox="0 0 114 114"><circle cx="57" cy="57" r="52" fill="none" stroke="#fff" stroke-width="7"/><polygon points="44,34 44,80 82,57" fill="#fff"/></svg>
    <h1>EXPERIENCE – <em>STRATEGY</em> – VISION</h1>
    <p>Velmora Partners is a vertically integrated real estate investment firm with a proven four-decade track record. We acquire, reposition, and operate high-performing assets across multiple sectors — always with a focus on exceptional, risk-adjusted returns.</p>
  </section>

  <!-- stats -->
  <svg class="abs" style="left:944px;top:921px" width="256" height="256"><polygon points="0,0 256,0 256,256" fill="#4a4a4c"/></svg>
  <svg class="abs" style="left:157px;top:985px" width="190" height="164"><polygon points="95,2 187,161 3,161" fill="none" stroke="#555" stroke-dasharray="3 2"/><polygon points="95,14 178,155 12,155" fill="#dc1e28"/><circle cx="95" cy="100" r="9" fill="#fff"/><rect x="80" y="112" width="30" height="16" rx="7" fill="#fff"/></svg>
  <svg class="abs" style="left:482px;top:985px" width="190" height="164"><polygon points="95,2 187,161 3,161" fill="none" stroke="#555" stroke-dasharray="3 2"/><polygon points="95,14 178,155 12,155" fill="#dc1e28"/><rect x="80" y="76" width="26" height="48" fill="none" stroke="#fff" stroke-width="3"/><line x1="64" y1="126" x2="126" y2="126" stroke="#fff" stroke-width="3"/></svg>
  <svg class="abs" style="left:821px;top:985px" width="190" height="164"><polygon points="95,2 187,161 3,161" fill="none" stroke="#555" stroke-dasharray="3 2"/><polygon points="95,14 178,155 12,155" fill="#dc1e28"/><path d="M68 104 L95 78 L122 104 M74 100 V130 H116 V100" fill="none" stroke="#fff" stroke-width="3"/></svg>
  <div class="abs stat" style="left:122px;top:1167px"><div class="num">40</div><div class="bar"></div><div class="lbl">Years of Operation<br>Founded: 1989</div></div>
  <div class="abs stat" style="left:447px;top:1167px"><div class="num">23,000+</div><div class="bar"></div><div class="lbl">Multifamily &amp; Healthcare<br>Units</div></div>
  <div class="abs stat" style="left:786px;top:1167px"><div class="num">$300+</div><div class="bar"></div><div class="lbl">Million Invested in<br>Enovations</div></div>

  <!-- sectors -->
  <svg class="abs" style="left:0;top:1322px" width="354" height="355"><polygon points="0,0 354,0 0,355" fill="#dc1e28"/></svg>
  <div class="abs sector" style="left:69px;width:346px;background:linear-gradient(180deg,#b9cde0 0%,#5d7590 45%,#2e3a48 100%)" role="img" aria-label="Glass office tower against a blue sky">
    <svg class="abs" style="left:0;top:159px" width="80" height="78"><polygon points="0,0 80,0 0,78" fill="#dc1e28"/></svg>
    <div class="band">OFFICE</div>
  </div>
  <div class="abs sector" style="left:427px;width:349px;background:linear-gradient(180deg,#7fb7e0 0%,#5b6a4a 35%,#3a4a3e 60%,#2a7fc0 100%)" role="img" aria-label="Residential complex with palm trees and a pool">
    <svg class="abs" style="left:0;top:159px" width="80" height="78"><polygon points="0,0 80,0 0,78" fill="#dc1e28"/></svg>
    <div class="band">MULTIFAMILY</div>
  </div>
  <div class="abs sector" style="left:786px;width:349px;background:linear-gradient(135deg,#e6e4e0 0%,#cfc9c0 50%,#a48a6c 100%)" role="img" aria-label="Interior under renovation with a wooden staircase">
    <div class="band">RENOVATIONS</div>
  </div>

  <!-- contact -->
  <section class="abs contact" role="img" aria-label="Modern house exterior at dusk">
    <svg class="abs" style="left:0;top:0" width="1200" height="639"><polygon points="508,0 562,0 1200,585 1200,639" fill="#8c8c8e" opacity=".75"/><polygon points="562,0 1200,0 1200,585" fill="#dc1e28" opacity=".82"/></svg>
    <svg class="abs" style="left:222px;top:168px" width="130" height="30"><polygon points="0,0 28,0 0,28" fill="#dc1e28"/><line x1="28" y1="1" x2="130" y2="1" stroke="#fff" stroke-width="2"/></svg>
    <h2>CONTACT <em>US</em></h2>
    <div class="field" style="left:110px;top:281px;width:552px;height:41px">Name:</div>
    <div class="field" style="left:110px;top:328px;width:268px;height:41px">Phone:</div>
    <div class="field" style="left:392px;top:328px;width:270px;height:41px">Email:</div>
    <div class="field" style="left:110px;top:376px;width:552px;height:75px">Mesage:</div>
    <div class="submit">SUBMIT<span class="ring"><svg width="18" height="18" viewBox="0 0 18 18"><path d="M4 14 L14 4 M7 4 H14 V11" fill="none" stroke="#fff" stroke-width="2.2"/></svg></span></div>
  </section>

  <!-- footer -->
  <footer class="abs footer">
    <svg class="abs" style="left:0;top:0" width="306" height="306"><polygon points="0,0 306,0 0,306" fill="#dc1e28"/></svg>
    <div class="foot-brand">VELMORA</div>
    <div class="info" style="left:228px"><div class="pin"><svg width="18" height="18" viewBox="0 0 18 18"><path d="M4 2 L7 2 L8 6 L6 7 Q8 11 11 12 L12 10 L16 11 L16 14 Q10 16 4 9 Q2 5 4 2Z" fill="#fff"/></svg></div><div>CALL US<br>014 220 5173</div></div>
    <div class="info" style="left:452px"><div class="pin"><svg width="18" height="14" viewBox="0 0 18 14"><rect x="1" y="1" width="16" height="12" fill="none" stroke="#fff" stroke-width="1.6"/><path d="M1 1l8 7 8-7" fill="none" stroke="#fff" stroke-width="1.6"/></svg></div><div>EMAIL US<br>info@velmora.com</div></div>
    <div class="info" style="left:759px"><div class="pin"><svg width="14" height="20" viewBox="0 0 14 20"><path d="M7 19 C2 12 1 9 1 7 A6 6 0 0 1 13 7 C13 9 12 12 7 19Z" fill="#fff"/><circle cx="7" cy="7" r="2.3" fill="#dc1e28"/></svg></div><div>ADDRESS<br>Harbor Point, NJ</div></div>
    <div class="rule" style="top:331px"></div>
    <div class="foot-nav"><span>Our Story</span><i>|</i><span>Investment Strategy</span><i>|</i><span>What Sets Us Apart</span><i>|</i><span>Our Portfolio</span><i>|</i><span>Contact</span></div>
    <div class="rule" style="top:409px"></div>
    <div class="copy">Copyright © 2025 All Rights Reserved By Company name</div>
    <div class="socials"><span></span><span></span><span></span><span></span></div>
  </footer>

</div>
</body>
</html>
```